Banner poster with different motifs

I'm looking for 5 banners and posters in A1 format in the same design, or the similarity must be recognizable...
Kept quite simple with different titles.

1 ballet
2 Contemporary Dance
3 high heels
4 Salsa & Bachata & Zouk
5 Hip Hop

Modern bright colors
it is for the entrance so that the students see here is a dance school

The text may also be included in the image
The photos are for guidance only; some are our own, some are purchased. However, we are permitted to use them, including our logo, of course.

```html
<!DOCTYPE html>
<html lang="en">
<head>
<meta charset="utf-8">
<title>Bailarosa Dance Center – Dance Poster</title>
<link href="https://fonts.googleapis.com/css2?family=Oswald:wght@700&family=Roboto:wght@300;400&display=swap" rel="stylesheet">
<style>
  :root {
    --backdrop: #d6d6d6;
    --paper: #fbfbfc;
    --ink: #1b1b1d;
    --accent-pink: #f07a8c;
    --accent-yellow: #eeea5c;
    --accent-green: #9bd466;
    --accent-blue: #29a9e1;
    --photo-light: #eef0f3;
    --photo-mid: #c9cdd3;
  }
  html, body {
    margin: 0;
    width: 1200px;
    height: 1200px;
    overflow: hidden;
    background: var(--backdrop);
  }
  .poster {
    position: absolute;
    left: 0;
    top: 177px;
    width: 1200px;
    height: 846px;
    background: var(--paper);
    overflow: hidden;
  }
  .poster-art {
    position: absolute;
    inset: 0;
    width: 1200px;
    height: 846px;
  }
  .brand {
    position: absolute;
    left: 132px;
    top: 62px;
    width: 268px;
    text-align: center;
    color: var(--ink);
    font-family: "Roboto", sans-serif;
    font-weight: 300;
  }
  .brand-dot {
    width: 96px;
    height: 96px;
    margin: 0 auto 14px;
    border: 2px solid var(--ink);
    border-radius: 50%;
  }
  .brand-name {
    font-size: 36px;
    letter-spacing: 3px;
    line-height: 1;
  }
  .brand-tagline {
    margin-top: 8px;
    font-size: 13px;
    letter-spacing: 3.2px;
    line-height: 1;
  }
  .class-list {
    position: absolute;
    left: 0;
    right: 0;
    top: 708px;
    text-align: center;
    font-family: "Roboto", sans-serif;
    font-weight: 400;
    font-size: 30px;
    line-height: 38px;
    color: var(--ink);
  }
  .class-list p { margin: 0; }
</style>
</head>
<body>
  <main class="poster">
    <svg class="poster-art" viewBox="0 0 1200 846" xmlns="http://www.w3.org/2000/svg">
      <defs>
        <radialGradient id="dancer-glow" cx="50%" cy="55%" r="55%">
          <stop offset="0%" stop-color="var(--photo-mid)" stop-opacity="0.55"/>
          <stop offset="100%" stop-color="var(--photo-light)" stop-opacity="0"/>
        </radialGradient>
        <radialGradient id="ribbon-tone" cx="50%" cy="50%" r="50%">
          <stop offset="0%" stop-color="var(--accent-blue)" stop-opacity="0.35"/>
          <stop offset="100%" stop-color="var(--accent-blue)" stop-opacity="0"/>
        </radialGradient>
        <linearGradient id="photo-ballet" gradientUnits="userSpaceOnUse" x1="0" y1="302" x2="0" y2="655">
          <stop offset="0%" stop-color="#f6eef0"/>
          <stop offset="55%" stop-color="#ecd9d6"/>
          <stop offset="100%" stop-color="#f2f2f2"/>
        </linearGradient>
        <linearGradient id="photo-contemporary" gradientUnits="userSpaceOnUse" x1="0" y1="302" x2="0" y2="655">
          <stop offset="0%" stop-color="#f4f1ec"/>
          <stop offset="45%" stop-color="#c9a27f"/>
          <stop offset="75%" stop-color="#7a5a44"/>
          <stop offset="100%" stop-color="#eeeeee"/>
        </linearGradient>
        <linearGradient id="photo-leap" gradientUnits="userSpaceOnUse" x1="0" y1="302" x2="0" y2="655">
          <stop offset="0%" stop-color="#eeeeee"/>
          <stop offset="40%" stop-color="#2a3140"/>
          <stop offset="65%" stop-color="#c89372"/>
          <stop offset="100%" stop-color="#e9e9ea"/>
        </linearGradient>
        <linearGradient id="photo-street" gradientUnits="userSpaceOnUse" x1="0" y1="302" x2="0" y2="655">
          <stop offset="0%" stop-color="#d8dbe0"/>
          <stop offset="50%" stop-color="#aeb3ba"/>
          <stop offset="100%" stop-color="#c7cbd1"/>
        </linearGradient>
        <linearGradient id="photo-hiphop" gradientUnits="userSpaceOnUse" x1="0" y1="302" x2="0" y2="655">
          <stop offset="0%" stop-color="#e4e6ea"/>
          <stop offset="50%" stop-color="#b9bcc2"/>
          <stop offset="100%" stop-color="#d5d7db"/>
        </linearGradient>
      </defs>

      <rect class="background-photo" x="290" y="110" width="650" height="736"
            fill="url(#dancer-glow)" role="img"
            aria-label="Faint photo of a dancer in white posing on the floor"/>

      <g class="accent-bars">
        <polygon points="192,280 340,280 184,600 53,600" fill="var(--accent-pink)" opacity="0.55"/>
        <polygon points="581,180 670,180 526,453 437,453" fill="var(--accent-yellow)" opacity="0.6"/>
        <polygon points="674,549 719,549 644,690 597,690" fill="var(--accent-green)" opacity="0.6"/>
      </g>

      <text class="headline" x="124" y="655" textLength="952" lengthAdjust="spacingAndGlyphs"
            font-family="Oswald, sans-serif" font-weight="700" font-size="436"
            fill-opacity="0.9" stroke="var(--ink)" stroke-width="2.5"
            role="img" aria-label="DANCE, each letter filled with a photo of a dancer: ballet, contemporary, leap, street and hip hop">
        <tspan fill="url(#photo-ballet)">D</tspan><tspan fill="url(#photo-contemporary)">A</tspan><tspan fill="url(#photo-leap)">N</tspan><tspan fill="url(#photo-street)">C</tspan><tspan fill="url(#photo-hiphop)">E</tspan>
      </text>

      <rect class="ribbon-ornament" x="794" y="52" width="350" height="210"
            fill="url(#ribbon-tone)" role="img"
            aria-label="Blue curling ribbon ornament"/>
    </svg>

    <div class="brand">
      <div class="brand-dot"></div>
      <div class="brand-name">BAILAROSA</div>
      <div class="brand-tagline">DANCE CENTER RIVERSIDE</div>
    </div>

    <div class="class-list">
      <p>Ballet • Contemporary Dance • High heels</p>
      <p>Salsa &amp; Bachata &amp; Zouk • Hip Hop</p>
    </div>
  </main>
</body>
</html>
```